Website for BQM CIVIL

looking for a clean crisp website outlining what we do, we are a telecommunications cable installer working on internet cabling, i am just looking for imagery and we will complete content

i need a

home page template
services tab (4 services)
Rod / Roping
Hauling
Civil
Surveying
Contact Us Page
Testimonials Page
About Us
Our Vision
History

Target Market(s)

Telecommunication Companies

Industry/Entity Type

Telecommunications

Requirements
Must have
• images and logo themed colors

this is main project we are working on

http://www.vorlyx.com.au/

this is an example of our competitor site in the same field, we are much smaller though

```html
<!DOCTYPE html>
<html lang="en">
<head>
<meta charset="utf-8">
<title>BQM CIVIL</title>
<link rel="stylesheet" href="https://fonts.googleapis.com/css2?family=Oswald:wght@300;400&family=Source+Sans+3:wght@400;600;700&display=swap">
<style>
  :root{
    --page-bg:#f5f5f5;
    --grid-line:rgba(0,0,0,.025);
    --ink:#2b2b2b;
    --body-ink:#3a3a3a;
    --nav-ink:#454545;
    --accent:#f07d1a;
    --brand-blue:#2e5c8a;
    --navy:#1f4f86;
    --panel:#e1e0e1;
    --video:#222222;
    --footer-ink:#555555;
    --social:#7a7a7a;
  }
  *{box-sizing:border-box;margin:0;padding:0}
  html,body{width:1200px;height:960px;overflow:hidden}
  body{
    position:relative;
    background-color:var(--page-bg);
    background-image:
      linear-gradient(var(--grid-line) 1px,transparent 1px),
      linear-gradient(90deg,var(--grid-line) 1px,transparent 1px);
    background-size:6px 6px;
    font-family:"Source Sans 3",sans-serif;
    color:var(--ink);
  }
  .brand{
    position:absolute;left:38px;top:56px;
    display:flex;align-items:center;gap:10px;
    font-family:"Source Sans 3",sans-serif;font-weight:700;
    font-size:44px;letter-spacing:1px;color:#1b1b1b;
  }
  .brand-dot{width:18px;height:18px;border-radius:50%;background:var(--accent)}
  .search{
    position:absolute;left:938px;top:39px;width:195px;height:28px;
    border:1px solid #e2e2e2;background:#f9f9f9;
  }
  .search svg{position:absolute;left:7px;top:8px}
  .main-nav{position:absolute;top:89px;left:0;width:1200px;height:42px;
    font-family:"Oswald",sans-serif;font-weight:400;font-size:27px;}
  .main-nav a{position:absolute;top:0;height:42px;line-height:42px;
    text-decoration:none;color:var(--nav-ink);transform:translateX(-50%);white-space:nowrap}
  .main-nav a.is-active{
    width:111px;text-align:center;color:var(--accent);
    background:linear-gradient(#dcdcdc,#cfcfcf);border:1px solid #bdbdbd;border-radius:3px;
  }
  .main-nav a.is-hover{color:var(--brand-blue)}
  .slider-arrow{position:absolute;top:296px}
  .hero-visual{
    position:absolute;left:311px;top:164px;width:575px;height:302px;
    background:linear-gradient(#d9d9d9,#f2f2f2 10%,#ffffff 60%,#cfcfcf);
    border-radius:14px 14px 40px 40px;
  }
  .about-panel{
    position:absolute;left:17px;top:489px;width:1162px;height:369px;
    background:var(--panel);box-shadow:0 6px 10px -4px rgba(0,0,0,.25);
  }
  .about-panel h2{position:absolute;left:41px;top:34px;font-size:31px;font-weight:700;color:var(--ink)}
  .about-panel p{
    position:absolute;left:43px;top:86px;width:610px;
    font-size:19px;line-height:22.5px;color:var(--body-ink);word-break:break-all;
  }
  .video{position:absolute;left:722px;top:31px;width:397px;height:267px;
    box-shadow:0 2px 4px rgba(0,0,0,.3)}
  .video-screen{height:242px;background:var(--video)}
  .video-controls{height:25px;background:linear-gradient(#f4f4f4,#d8d8d8);border-top:1px solid #bbb}
  .pager{position:absolute;left:1012px;top:344px;display:flex;gap:8px}
  .pager span{width:22px;height:6px;background:var(--navy)}
  .pager span.is-current{background:var(--accent)}
  .site-footer{position:absolute;left:36px;top:878px;font-family:"Oswald",sans-serif;font-weight:300;color:var(--footer-ink)}
  .footer-nav{font-size:18px}
  .footer-nav a{color:var(--footer-ink);text-decoration:none}
  .footer-nav .sep{margin:0 6px}
  .copyright{margin-top:8px;font-size:15px}
  .social{position:absolute;top:886px;display:flex;gap:40px;left:960px;
    font-family:"Source Sans 3",sans-serif;font-weight:700;font-size:20px;color:var(--social)}
</style>
</head>
<body>
  <header>
    <div class="brand"><span class="brand-dot"></span>BQM CIVIL</div>
    <div class="search">
      <svg width="12" height="12" viewBox="0 0 12 12"><circle cx="5" cy="5" r="3.5" fill="none" stroke="#bbb" stroke-width="1.5"/><line x1="7.5" y1="7.5" x2="11" y2="11" stroke="#bbb" stroke-width="1.5"/></svg>
    </div>
    <nav class="main-nav">
      <a href="#" class="is-active" style="left:418px">HOME</a>
      <a href="#" class="is-hover" style="left:557px">ABOUT</a>
      <a href="#" style="left:708px">SERVICES</a>
      <a href="#" style="left:897px">TESTIMONIALS</a>
      <a href="#" style="left:1093px">CONTACT</a>
    </nav>
  </header>

  <section class="hero">
    <svg class="slider-arrow" style="left:175px" width="20" height="28" viewBox="0 0 20 28"><path d="M15 3 L5 14 L15 25" fill="none" stroke="#3a3a3a" stroke-width="5" stroke-linecap="round" stroke-linejoin="round"/></svg>
    <div class="hero-visual" role="img" aria-label="Laptop showing a line chart of network growth"></div>
    <svg class="slider-arrow" style="left:1011px" width="20" height="28" viewBox="0 0 20 28"><path d="M5 3 L15 14 L5 25" fill="none" stroke="#3a3a3a" stroke-width="5" stroke-linecap="round" stroke-linejoin="round"/></svg>
  </section>

  <section class="about-panel">
    <h2>Who We Are ?</h2>
    <p>Lorem Ipsum is simply dummy text of the printing and typesetting industry. Lorem Ipsum has been the industry's standard dummy text ever since the 1500s, when an unknown printer took a galley of type and scrambled it to make a type specimen book. It has survived not only five centuries, but also the leap into electronic typesetting, remaining essentially unchanged. It was popularised in the 1960s with the release of Letterline sheets containing Lorem Ipsum passages, and more recently with desktop publishing software like Alder PageSetter including versions of Lorem Ipsum.</p>
    <div class="video">
      <div class="video-screen"></div>
      <svg class="video-controls" width="397" height="25" viewBox="0 0 397 25">
        <path d="M12 7 L21 12.5 L12 18 Z" fill="#555"/>
        <rect x="36" y="9" width="212" height="7" rx="3.5" fill="#666"/>
        <rect x="36" y="9" width="140" height="7" rx="3.5" fill="#888"/>
        <rect x="36" y="9" width="104" height="7" rx="3.5" fill="#e0403e"/>
        <circle cx="140" cy="12.5" r="5" fill="#eee" stroke="#999"/>
        <text x="256" y="16" font-family="Source Sans 3, sans-serif" font-size="8" fill="#555">3.47 / 9.29</text>
        <path d="M312 10 h3 l4 -3 v11 l-4 -3 h-3 Z" fill="#555"/>
        <rect x="330" y="9" width="54" height="7" rx="3.5" fill="#555"/>
        <circle cx="380" cy="12.5" r="4" fill="#eee" stroke="#777"/>
      </svg>
    </div>
    <div class="pager"><span class="is-current"></span><span></span><span></span><span></span></div>
  </section>

  <footer class="site-footer">
    <nav class="footer-nav">
      <a href="#">Home</a><span class="sep">|</span><a href="#">About</a><span class="sep">|</span><a href="#">Services</a><span class="sep">|</span><a href="#">Testimonials</a><span class="sep">|</span><a href="#">Contact</a><span class="sep">|</span><a href="#">Sitemap</a>
    </nav>
    <div class="copyright">Copyright 2013 - BQM Civil</div>
  </footer>
  <div class="social"><span>Chirper</span><span>Tumbleweave</span></div>
</body>
</html>
```